Bref créative |
Business Cards for hardscaping company | ||
Brennock Stoneworks LLC | ||
Use same font as used in my logo | ||
Cutting-Edge Corporate Traditional Modern Professional Simple Bright & Fun-filled |
Dwight Halvorsen | ||
Owner | ||
412 Tollivar Mill Road Chadds Ford, PA 19342 |
brennockstoneworks@quillmarsh.com | ||
Please add the line (all phases of hardscape construction & Snow Removal) | ||

```html
<!DOCTYPE html>
<html lang="en">
<head>
<meta charset="utf-8">
<title>Brennock Stoneworks LLC – Business Cards</title>
<link rel="stylesheet" href="https://fonts.googleapis.com/css2?family=Cinzel:wght@600&family=Lato:wght@400;700&display=swap">
<style>
  :root {
    --page-bg: #e9e7e3;
    --card-black: #0b0b0d;
    --brand-blue: #8fb0e6;
    --wave-blue: #7aa7e8;
    --wave-grey: #8b8f96;
    --text-light: #d9dce2;
    --text-muted: #9aa0aa;
    --rule: #5d626b;
  }
  * { box-sizing: border-box; margin: 0; padding: 0; }
  html, body { width: 1200px; height: 629px; overflow: hidden; }
  body {
    background: var(--page-bg);
    font-family: "Lato", Arial, sans-serif;
    position: relative;
  }
  .card {
    position: absolute;
    top: 160px;
    width: 540px;
    height: 309px;
    background: var(--card-black);
    border-radius: 4px;
    overflow: hidden;
    box-shadow: 0 6px 18px rgba(0,0,0,.22);
  }
  .card--front { left: 40px; }
  .card--back { left: 620px; }

  .brand { text-align: center; color: var(--brand-blue); font-family: "Cinzel", Georgia, serif; font-weight: 600; line-height: 1; }
  .brand__primary { display: block; font-size: 44px; letter-spacing: 2px; }
  .brand__secondary { display: block; font-size: 20px; letter-spacing: 6px; margin-top: 6px; }
  .tagline { margin-top: 10px; font-size: 9px; letter-spacing: 1.2px; text-transform: uppercase; color: var(--text-muted); text-align: center; }

  .card--front .brand-block { position: absolute; top: 50%; left: 50%; transform: translate(-50%, -50%); width: 420px; }

  .card--back .brand-block { position: absolute; left: 44px; top: 78px; width: 250px; }
  .card--back .brand__primary { font-size: 34px; }
  .card--back .brand__secondary { font-size: 15px; letter-spacing: 4.5px; }
  .card--back .tagline { font-size: 7px; letter-spacing: .6px; }

  .divider { position: absolute; left: 312px; top: 74px; width: 1px; height: 108px; background: var(--rule); }

  .contact { position: absolute; left: 330px; top: 84px; list-style: none; }
  .contact__item { display: flex; align-items: center; gap: 8px; font-size: 10px; color: var(--text-light); margin-bottom: 9px; line-height: 1.25; }
  .contact__icon { width: 12px; height: 12px; flex: none; }

  .holder { position: absolute; left: 44px; bottom: 44px; font-size: 11px; letter-spacing: 1.4px; color: var(--text-light); text-transform: uppercase; }
  .holder__sep { color: var(--text-muted); margin: 0 8px; }

  .wave { position: absolute; right: 0; bottom: 0; width: 540px; height: 309px; }
</style>
</head>
<body>
  <section class="card card--front" aria-label="Card front">
    <div class="brand-block">
      <p class="brand"><span class="brand__primary">BRENNOCK</span><span class="brand__secondary">STONEWORKS</span></p>
      <p class="tagline">All phases of hardscape construction &amp; snow removal</p>
    </div>
  </section>

  <section class="card card--back" aria-label="Card back">
    <svg class="wave" viewBox="0 0 540 309" aria-hidden="true">
      <path d="M110 309 C260 300 360 260 430 218 C480 188 515 170 540 166 L540 309 Z" fill="var(--wave-grey)"/>
      <path d="M160 309 C290 302 380 270 445 232 C490 205 520 190 540 186 L540 309 Z" fill="var(--card-black)"/>
      <path d="M230 309 C330 302 410 278 465 250 C500 232 525 222 540 219 L540 309 Z" fill="var(--wave-blue)"/>
    </svg>

    <div class="brand-block">
      <p class="brand"><span class="brand__primary">BRENNOCK</span><span class="brand__secondary">STONEWORKS</span></p>
      <p class="tagline">All phases of hardscape construction &amp; snow removal</p>
    </div>

    <div class="divider"></div>

    <ul class="contact">
      <li class="contact__item">
        <svg class="contact__icon" viewBox="0 0 12 12"><path d="M6 1a3.5 3.5 0 0 0-3.5 3.5C2.5 7.3 6 11 6 11s3.5-3.7 3.5-6.5A3.5 3.5 0 0 0 6 1zm0 4.8a1.3 1.3 0 1 1 0-2.6 1.3 1.3 0 0 1 0 2.6z" fill="var(--text-light)"/></svg>
        <span>412 Tollivar Mill Road<br>Chadds Ford, PA 19342</span>
      </li>
      <li class="contact__item">
        <svg class="contact__icon" viewBox="0 0 12 12"><path d="M3 1.2l1.6 2.2-.9 1.2c.6 1.3 1.5 2.2 2.7 2.8l1.2-.9 2.2 1.6-.8 1.9C5.3 10 2 6.7 2 2z" fill="var(--text-light)"/></svg>
        <span>(610) 555-0148</span>
      </li>
      <li class="contact__item">
        <svg class="contact__icon" viewBox="0 0 12 12"><rect x="1" y="2.5" width="10" height="7" rx="1" fill="none" stroke="var(--text-light)"/><path d="M1.5 3l4.5 3.5L10.5 3" fill="none" stroke="var(--text-light)"/></svg>
        <span>brennockstoneworks@quillmarsh.com</span>
      </li>
    </ul>

    <p class="holder">Dwight Halvorsen<span class="holder__sep">|</span>Owner</p>
  </section>
</body>
</html>
```